Luxury Eye Cream Label

Velmora Skin is developing a line of luxury dermatology creams designed to improve and treat various skin conditions and esthetic problems.
All creams are handmade by registered pharmacies according to patient needs, on the same day of the order. (meaning the creams are not premade. the creams are freshly made without any preservatives or stabilizers.)
The labels are two. One for the upper lid of an aluminum container 4.0 cm. in diameter containing company logo and description of the cream. The other one is for the bottom of the container 4.0 in diameter containing pharmacy information.
The label should convey professional, MD, and luxury feel.
(Upper Lid Label)
Logo of velmora skin
EYE CARE CREAM - intensive
Doctor Series
handmade . Doctor formulated . registered Pharmacy . highest ethical standards . (in a circular pattern on the label)
Ingredients: Marigold extract, Witch Hazel Distillate, Water, Glycerin, Stearyl Alcohol, Wheat Germ Oil, Polysorbate 60, Sesame Oil, Myristyl Myristate, Cetyl Alcohol, Sorbitan Stearate, Phenoxyethanol, Calendula Extract, Cornflower Extract, Sodium Alginate, Sodium Citrate, Mica, Vit. C, Vit. E.
Please, adhere to the above content, and dimension of the label of 4 cm in diameter. Also, please view it to scale. This is a relatively small container, aluminum ½ ounce (15ml) cream.
The Bottom of the Jar will have a label with the following information. This is obligatory, because of regulatory requirements for any product prepared by a pharmacy.
I understand that the space is limited. The background should be a lighter color, and the pharmacist will hand write the information (with a darker color marker).
EXTERNAL USE
Pharmacy: Pelaro, 18 Blvd. Ts. Orlinov, Sofia 1157, ph. 02 9473615
Rx No. Date
Patient Name age
Pharmacist Good until:
Please, view it to scale of 4 cm in diameter (which is the actual label of the Face Cream Intense), so you will have a better feeling of the design.
Thank you so much.

```html
<!DOCTYPE html>
<html lang="en">
<head>
<meta charset="utf-8">
<title>Velmora Skin – Eye Care Cream Labels</title>
<link rel="stylesheet" href="https://fonts.googleapis.com/css2?family=Marcellus+SC&family=Open+Sans:wght@400;600&display=swap">
<style>
  :root {
    --page: #ffffff;
    --ink: #111111;
    --label: #808184;
    --label-text: #ffffff;
    --gold: #c9a062;
    --script-band: #c9c9cb;
  }
  html, body {
    margin: 0;
    padding: 0;
    width: 1200px;
    height: 1000px;
    overflow: hidden;
    background: var(--page);
  }
  .sheet {
    position: relative;
    width: 1200px;
    height: 1000px;
  }
  .section-title {
    position: absolute;
    left: 0;
    width: 1200px;
    margin: 0;
    text-align: center;
    font-family: "Marcellus SC", serif;
    font-weight: 400;
    font-size: 46px;
    letter-spacing: 1px;
    color: var(--ink);
  }
  .section-title--preview { top: 28px; }
  .section-title--real { top: 712px; }
  .artboard {
    position: absolute;
    left: 0;
    top: 0;
  }
  .label-disc { fill: var(--label); }
  .ring-text {
    font-family: "Open Sans", sans-serif;
    font-size: 31px;
    fill: var(--label-text);
  }
  .brand-name {
    font-family: "Open Sans", sans-serif;
    font-size: 34px;
    fill: var(--gold);
  }
  .brand-dot {
    fill: none;
    stroke: var(--gold);
    stroke-width: 2;
  }
  .script-band { fill: var(--script-band); }
  .product-type {
    font-family: "Marcellus SC", serif;
    font-size: 24px;
    letter-spacing: 3px;
    fill: var(--label-text);
  }
  .product-variant {
    font-family: "Marcellus SC", serif;
    font-size: 34px;
    letter-spacing: 6px;
    fill: var(--label-text);
  }
  .base-heading {
    font-family: "Marcellus SC", serif;
    font-size: 33px;
    letter-spacing: 1px;
    fill: var(--label-text);
  }
  .base-pharmacy {
    font-family: "Marcellus SC", serif;
    font-size: 21px;
    fill: var(--label-text);
  }
  .base-field {
    font-family: "Marcellus SC", serif;
    font-size: 21px;
    fill: var(--label-text);
  }
</style>
</head>
<body>
<main class="sheet">
  <h1 class="section-title section-title--preview">Preview version</h1>
  <h2 class="section-title section-title--real">Real size version</h2>

  <svg class="artboard" width="1200" height="1000" viewBox="0 0 1200 1000" aria-label="Lid and base labels for Velmora Skin eye care cream">
    <defs>
      <path id="ring-path" d="M -171 83 A 190 190 0 0 1 171 -83 A 190 190 0 0 1 -171 83"/>

      <g id="lid-label">
        <circle class="label-disc" r="226"/>
        <text class="ring-text">
          <textPath href="#ring-path" textLength="1150" lengthAdjust="spacing">highest ethical standards • handmade • doctor formulated • registered pharmacy •</textPath>
        </text>
        <g role="img" aria-label="Hand-lettered line reading Doctor Series">
          <rect class="script-band" x="-140" y="-86" width="280" height="30" rx="4"/>
        </g>
        <circle class="brand-dot" cx="-128" cy="2" r="20"/>
        <text class="brand-name" x="18" y="14" text-anchor="middle">velmora skin</text>
        <text class="product-type" x="0" y="76" text-anchor="middle">Eye care cream</text>
        <text class="product-variant" x="0" y="112" text-anchor="middle">Intensive</text>
      </g>

      <g id="base-label">
        <circle class="label-disc" r="228"/>
        <text class="base-heading" x="0" y="-125" text-anchor="middle">EXTERNAL USE</text>
        <text class="base-pharmacy" x="0" y="-88" text-anchor="middle">Pharmacy: Pelaro, 18 Blvd. Ts. Orlinov,</text>
        <text class="base-pharmacy" x="0" y="-64" text-anchor="middle">Sofia 1157, ph. 02 9473615</text>
        <text class="base-field" x="-177" y="-22">Rx No.</text>
        <text class="base-field" x="-177" y="7">Date</text>
        <text class="base-field" x="-177" y="36">Patient Name</text>
        <text class="base-field" x="-177" y="65">Age</text>
        <text class="base-field" x="-177" y="123">Pharmacist Good until:</text>
      </g>
    </defs>

    <use href="#lid-label" transform="translate(328 400)"/>
    <use href="#base-label" transform="translate(853 403)"/>

    <use href="#lid-label" transform="translate(536 869) scale(0.262)"/>
    <use href="#base-label" transform="translate(667 869) scale(0.257)"/>
  </svg>
</main>
</body>
</html>
```